Custom LED sign business needs logo and web design.

We need a logo and website design for a new company based in Austin TX. What we do is laser engrave custom artwork for led edge lit signs. Our marketing will be directed to kids rooms, game rooms and business. I would like to see designs that have a neon text effect. The look should feel professional for businesses and fun for kids.

**UPDATE** This website will need a custom design page that uses Quillmark Item Composer type plugin. The users will be able to choose from pre-loaded artwork and fonts or upload there own artwork.
There will also be a ecommerce tab that will. have ready to ship signs available.
Wordpress will be the platform used.

Target Market(s)

Businesses, kids and game rooms

Neon Text effect with logo. Professional but fun.

Logo Text

Vorbrights

Number of Pages Required

5+ page

Font styles to use
Other font styles liked:
• A neon text effect type font. Example picture added

Colors

Designer to choose colors to be used in the design.

Requirements
Must have
• Neon Text effects with a professional tech look. Incorporate the "create", "energize" and "amaze" as the company slogan.
• Quillmark Item Composer for customer interactive sign design.
• Ecommerce platform so that I can upload ready to ship signs.
• Refer to the Create, Energize, Amaze pics attached as company slogan. Use those fonts.
Nice to have
• I would like text to "turn on" when hovered over.
Should not have
• Scattered text locations. Unorganized layout and feel.

```html
<!DOCTYPE html>
<html lang="en">
<head>
<meta charset="utf-8">
<title>Vorbrights — Custom LED Signs</title>
<link rel="stylesheet" href="https://fonts.googleapis.com/css2?family=Arimo:wght@400;700&display=swap">
<style>
:root{
  --bg:#000000;
  --brick:#1c1a19;
  --brick-light:#2b2826;
  --neon:#ff2f8e;
  --neon-soft:#ff7ab8;
  --neon-glow:rgba(255,47,142,.75);
  --btn-fill:#2a1522;
  --text:#ffffff;
  --muted:#b5b5b5;
  --rule:#2a2a2a;
  --frame:#5a5a5a;
}
*{box-sizing:border-box;margin:0;padding:0}
html,body{width:1200px;height:2761px;overflow:hidden;background:var(--bg)}
body{position:relative;font-family:"Arimo",Arial,sans-serif;color:var(--text)}
.abs{position:absolute}

/* hero */
.hero{left:0;top:0;width:1200px;height:548px;
  background:radial-gradient(ellipse at 50% 20%,var(--brick-light) 0%,var(--brick) 45%,#080808 100%)}
.brand-name{color:var(--neon);font-weight:700;white-space:nowrap}
.hero .brand-name{left:0;width:1200px;top:62px;text-align:center;font-size:76px}
.hero-title{left:0;width:1200px;top:286px;text-align:center;font-size:33px;font-weight:700}
.hero-copy{left:244px;width:752px;top:346px;text-align:center;font-size:8.6px;line-height:11px}

.neon-btn{display:flex;align-items:center;justify-content:center;color:var(--neon-soft);
  background:var(--btn-fill);border:2px solid var(--neon);border-radius:7px;
  box-shadow:0 0 8px var(--neon-glow),inset 0 0 5px var(--neon-glow);font-weight:700;text-decoration:none}
.hero .neon-btn{left:484px;top:442px;width:245px;height:39px;font-size:14px}

/* about */
.section-title{font-size:32px;font-weight:700}
.about-title{left:86px;top:592px}
.about-copy{left:86px;top:640px;width:422px;font-size:8.6px;line-height:11px;font-weight:700}
.about .neon-btn{left:88px;top:762px;width:245px;height:40px;font-size:14px}
.about-photo{left:674px;top:595px;width:427px;height:246px;border:3px solid var(--frame);
  background:radial-gradient(circle at 30% 40%,#1f7a5a 0%,transparent 30%),radial-gradient(circle at 55% 35%,#6b2ca0 0%,transparent 22%),radial-gradient(circle at 85% 40%,#2b6bd1 0%,transparent 22%),linear-gradient(180deg,#4a4d52 0%,#1b1c1e 60%,#2e2b28 100%)}

/* products */
.center-title{left:0;width:1200px;text-align:center}
.products-title{top:918px}
.section-sub{left:0;width:1200px;text-align:center;font-size:13px;font-weight:700;color:var(--muted)}
.products-sub{top:968px}
.product{width:257px}
.product-photo{width:257px;height:198px;border:2px solid var(--frame)}
.product-caption{margin-top:8px;font-size:10.5px;line-height:12px;color:var(--muted)}
.product .neon-btn{margin-top:8px;width:109px;height:16px;font-size:5.5px;border-width:1.5px;border-radius:3px;box-shadow:0 0 4px var(--neon-glow)}

/* contact */
.contact-title{top:1972px}
.contact-sub{top:2022px}
.field{left:408px;width:375px;border:2.5px solid var(--neon);border-radius:8px;
  box-shadow:0 0 10px var(--neon-glow),inset 0 0 6px var(--neon-glow);
  color:var(--muted);font-style:italic;font-size:13px;text-align:center}
.field-name{top:2081px;height:49px;line-height:44px}
.field-email{top:2153px;height:48px;line-height:52px}
.field-message{top:2223px;height:102px;padding-top:6px}
.submit-btn{left:475px;top:2348px;width:242px;height:49px;font-size:15px;font-weight:400;color:var(--text);background:#100608}

/* footer */
.footer-rule{left:0;top:2522px;width:1200px;height:1px;background:var(--rule)}
.footer .brand-name{left:116px;top:2600px;font-size:46px}
.footer-col{top:2566px}
.footer-col h3{font-size:21px;font-weight:700;color:#d6d6d6;margin-bottom:10px}
.footer-col li{list-style:none;font-size:14.5px;line-height:19px;color:#8d8d8d}
</style>
</head>
<body>

<header class="hero abs">
  <div class="brand-name abs">Vorbrights</div>
  <h1 class="hero-title abs">Lorem ipsum dolor sit amet,</h1>
  <p class="hero-copy abs">Lorem ipsum dolor sit amet, consectetuer adipiscing elit, sed diam nonummy nibh euismod tincidunt ut laoreet dolore magna aliquam erat volutpat. Ut wisi enim ad minim veniam, quis nostrud exerci tation ullamcorper suscipit lobortis nisl ut aliquip ex ea commodo consequat. Duis autem vel eum iriure dolor in hendrerit in vulputate velit esse molestie consequat, vel illum dolore eu feugiat nulla facilisis at vero eros et accumsan et iusto odio dignissim qui blandit praesent luptatum.</p>
  <a class="neon-btn abs" href="#">See More...</a>
</header>

<section class="about">
  <h2 class="section-title about-title abs">ABOUT US</h2>
  <p class="about-copy abs">Lorem ipsum dolor sit amet, consectetuer adipiscing elit, sed diam nonummy nibh euismod tincidunt ut laoreet dolore magna aliquam erat volutpat. Ut wisi enim ad minim veniam, quis nostrud exerci tation ullamcorper suscipit lobortis nisl ut aliquip ex ea commodo consequat. Duis autem vel eum iriure dolor in hendrerit in vulputate velit esse molestie consequat.<br>Lorem ipsum dolor sit amet, cons ectetuer adipiscing elit, sed diam nonummy nibh euismod tincidunt ut laoreet dolore magna aliquam erat volutpat.</p>
  <a class="neon-btn abs" href="#">See More...</a>
  <div class="about-photo abs" role="img" aria-label="Photo of five edge-lit acrylic signs glowing green, purple, red and blue on wooden bases beside pebbles"></div>
</section>

<section class="products">
  <h2 class="section-title center-title products-title abs">PRODUCTS</h2>
  <p class="section-sub products-sub abs">Lorem ipsum dolor sit amet, consectetuer adipiscing elit, sed diam nonummy nibh euis</p>

  <div class="product abs" style="left:71px;top:1042px"><div class="product-photo" role="img" aria-label="Blue edge-lit sign with a hot rod car and award lettering" style="background:radial-gradient(circle at 50% 50%,#1f4fd8 0%,#0a1a5a 50%,#02030a 100%)"></div><p class="product-caption">Lorem ipsum dolor sit amet, consectetuer adipiscing elit, sed diam nonummy nibh euis</p><a class="neon-btn" href="#">See More...</a></div>
  <div class="product abs" style="left:340px;top:1042px"><div class="product-photo" role="img" aria-label="Clear engraved sign of a touring motorcycle on a wooden base" style="background:linear-gradient(180deg,#1a1a1a 0%,#0a0a0a 70%,#5a3416 100%)"></div><p class="product-caption">Lorem ipsum dolor sit amet, consectetuer adipiscing elit, sed diam nonummy nibh euis</p><a class="neon-btn" href="#">See More...</a></div>
  <div class="product abs" style="left:607px;top:1042px"><div class="product-photo" role="img" aria-label="Blue edge-lit sign of a convertible car" style="background:radial-gradient(circle at 50% 50%,#2a45e0 0%,#0b1670 55%,#020418 100%)"></div><p class="product-caption">Lorem ipsum dolor sit amet, consectetuer adipiscing elit, sed diam nonummy nibh euis</p><a class="neon-btn" href="#">See More...</a></div>
  <div class="product abs" style="left:875px;top:1042px"><div class="product-photo" role="img" aria-label="Blue edge-lit sign of a vintage truck" style="background:radial-gradient(circle at 50% 50%,#1d3dd0 0%,#081262 55%,#020316 100%)"></div><p class="product-caption">Lorem ipsum dolor sit amet, consectetuer adipiscing elit, sed diam nonummy nibh euis</p><a class="neon-btn" href="#">See More...</a></div>

  <div class="product abs" style="left:71px;top:1352px"><div class="product-photo" role="img" aria-label="White neon script sign above shelves with plants and a framed print" style="background:linear-gradient(180deg,#9a9a96 0%,#6f6e6a 55%,#3a3a38 100%)"></div><p class="product-caption">Lorem ipsum dolor sit amet, consectetuer adipiscing elit, sed diam nonummy nibh euis</p><a class="neon-btn" href="#">See More...</a></div>
  <div class="product abs" style="left:340px;top:1352px"><div class="product-photo" role="img" aria-label="Pink neon sign on a pink wall above a sofa" style="background:linear-gradient(180deg,#d8476f 0%,#b02a4f 60%,#3a1a20 100%)"></div><p class="product-caption">Lorem ipsum dolor sit amet, consectetuer adipiscing elit, sed diam nonummy nibh euis</p><a class="neon-btn" href="#">See More...</a></div>
  <div class="product abs" style="left:607px;top:1352px"><div class="product-photo" role="img" aria-label="Cloud-shaped neon light above a lounge chair" style="background:linear-gradient(180deg,#d9cfc2 0%,#b3a390 60%,#7a5a3c 100%)"></div><p class="product-caption">Lorem ipsum dolor sit amet, consectetuer adipiscing elit, sed diam nonummy nibh euis</p><a class="neon-btn" href="#">See More...</a></div>
  <div class="product abs" style="left:875px;top:1352px"><div class="product-photo" role="img" aria-label="Living room with a small neon sign on a yellow shelf" style="background:linear-gradient(180deg,#e6e0d8 0%,#cfc4b6 60%,#a89886 100%)"></div><p class="product-caption">Lorem ipsum dolor sit amet, consectetuer adipiscing elit, sed diam nonummy nibh euis</p><a class="neon-btn" href="#">See More...</a></div>

  <div class="product abs" style="left:71px;top:1656px"><div class="product-photo" role="img" aria-label="Kids bedroom with colourful game-themed neon lights above a bed" style="background:linear-gradient(180deg,#d6d6d8 0%,#a8a8ac 55%,#3c6a3a 100%)"></div><p class="product-caption">Lorem ipsum dolor sit amet, consectetuer adipiscing elit, sed diam nonummy nibh euis</p><a class="neon-btn" href="#">See More...</a></div>
  <div class="product abs" style="left:340px;top:1656px"><div class="product-photo" role="img" aria-label="Round neon sign with palm tree and cocktail on a dark wall" style="background:radial-gradient(circle at 50% 45%,#6a3a8a 0%,#2a1a3a 45%,#0e0c14 100%)"></div><p class="product-caption">Lorem ipsum dolor sit amet, consectetuer adipiscing elit, sed diam nonummy nibh euis</p><a class="neon-btn" href="#">See More...</a></div>
  <div class="product abs" style="left:607px;top:1656px"><div class="product-photo" role="img" aria-label="Blue octopus neon sign on a grey wall" style="background:radial-gradient(circle at 50% 45%,#3f5bd6 0%,#2b2f4a 45%,#1a1a1e 100%)"></div><p class="product-caption">Lorem ipsum dolor sit amet, consectetuer adipiscing elit, sed diam nonummy nibh euis</p><a class="neon-btn" href="#">See More...</a></div>
  <div class="product abs" style="left:875px;top:1656px"><div class="product-photo" role="img" aria-label="White neon script sign on a dark brick wall" style="background:radial-gradient(circle at 50% 45%,#4a4a52 0%,#1e1e22 55%,#0c0c0e 100%)"></div><p class="product-caption">Lorem ipsum dolor sit amet, consectetuer adipiscing elit, sed diam nonummy nibh euis</p><a class="neon-btn" href="#">See More...</a></div>
</section>

<section class="contact">
  <h2 class="section-title center-title contact-title abs">CONTACT US</h2>
  <p class="section-sub contact-sub abs">Lorem ipsum dolor sit amet, consectetuer adipiscing elit, sed diam nonummy nibh euis</p>
  <div class="field field-name abs">name</div>
  <div class="field field-email abs">email</div>
  <div class="field field-message abs">message</div>
  <a class="neon-btn submit-btn abs" href="#">SUBMIT</a>
</section>

<footer class="footer">
  <div class="footer-rule abs"></div>
  <div class="brand-name abs">Vorbrights</div>
  <div class="footer-col abs" style="left:381px"><h3>Info</h3><ul><li>Stocklist</li><li>Lorem Ip</li><li>Ipsun dol</li><li>Privacy Policy</li><li>Terms &amp; Cond.</li></ul></div>
  <div class="footer-col abs" style="left:524px"><h3>Menu</h3><ul><li>Home</li><li>About Us</li><li>Products</li><li>Contact Us</li></ul></div>
  <div class="footer-col abs" style="left:654px"><h3>Links</h3><ul><li>Link 1</li><li>Link 2</li><li>Link 3</li><li>Link 4</li></ul></div>
  <div class="footer-col abs" style="left:776px"><h3>Social</h3><ul><li>Friendwall</li><li>Chirpline</li><li>Snapgrid</li><li>Clipstream</li></ul></div>
</footer>

</body>
</html>
```